Business Carss for Harborview Church

Need a progressive looking/modern business card design for my church

Target Market(s)

Families and young adults

Industry/Entity Type

Religious

Contact Information for Business Card

2846 Willow Creek Rd.
Frankfort Ky
502-555-0147

Rev. Curtis Holloway
Slogan: Honor God and Make Discies

Font styles to use
Serif
Sans Serif
Decorative
Script

Colors
0555a3
3176b5

Requirements
Should not have
• Should not have a template look
• A unique out of the box look

```html
<!DOCTYPE html>
<html lang="en">
<head>
<meta charset="utf-8">
<title>Harborview Church – Business Cards</title>
<link href="https://fonts.googleapis.com/css2?family=Roboto:wght@300;700&family=Open+Sans:wght@400;700&display=swap" rel="stylesheet">
<style>
  :root {
    --deep-blue: #0555a3;
    --mid-blue: #3176b5;
    --white: #ffffff;
    --page: #e7e9ec;
  }
  * { margin: 0; padding: 0; box-sizing: border-box; }
  html, body {
    width: 1200px;
    height: 1200px;
    overflow: hidden;
    background: var(--page);
  }
  .sheet {
    position: relative;
    width: 1200px;
    height: 1200px;
  }
  .card {
    position: absolute;
    left: 200px;
    width: 800px;
    height: 456px;
    border-radius: 29px;
    overflow: hidden;
    color: var(--white);
  }
  .card--front { top: 80px; background: var(--deep-blue); }
  .card--back  { top: 664px; background: var(--mid-blue); }

  .identity {
    position: absolute;
    left: 52px;
    top: 142px;
  }
  .identity__name {
    font-family: "Roboto", sans-serif;
    font-weight: 700;
    font-size: 37px;
    line-height: 1.1;
    letter-spacing: -0.2px;
  }
  .identity__slogan {
    margin-top: 6px;
    font-family: "Roboto", sans-serif;
    font-weight: 300;
    font-size: 18.5px;
  }

  .contact-panel {
    position: absolute;
    left: 436px;
    top: 77px;
    width: 334px;
    height: 301px;
    box-shadow: -5px 0 8px -4px rgba(0, 0, 0, 0.35);
  }
  .card--front .contact-panel { background: var(--mid-blue); }
  .card--back  .contact-panel { background: var(--deep-blue); }

  .contact-row {
    position: absolute;
    left: 50px;
    display: flex;
    align-items: center;
    gap: 19px;
    font-family: "Open Sans", sans-serif;
  }
  .contact-row--address { top: 79px; }
  .contact-row--phone   { top: 182px; }

  .contact-icon {
    width: 42px;
    height: 42px;
    flex: none;
  }
  .contact-text--address {
    font-size: 18.5px;
    font-weight: 400;
    line-height: 1.35;
    text-transform: uppercase;
  }
  .contact-text--phone {
    font-size: 21px;
    font-weight: 700;
  }
</style>
</head>
<body>
<main class="sheet">

  <section class="card card--front" aria-label="Business card, dark blue version">
    <div class="identity">
      <h1 class="identity__name">Rev. Curtis Holloway</h1>
      <p class="identity__slogan">Honor God and Make Discies</p>
    </div>
    <div class="contact-panel">
      <div class="contact-row contact-row--address">
        <svg class="contact-icon" viewBox="0 0 42 42" aria-hidden="true">
          <rect x="2" y="2" width="38" height="38" rx="8" fill="none" stroke="#fff" stroke-width="3"/>
          <path d="M21 9 L32 19 H29 V31 H13 V19 H10 Z" fill="#fff"/>
          <rect x="16" y="21" width="4" height="4" fill="#3176b5"/>
          <rect x="22" y="21" width="4" height="4" fill="#3176b5"/>
        </svg>
        <p class="contact-text contact-text--address">2846 Willow Creek Rd.<br>Frankfort KY</p>
      </div>
      <div class="contact-row contact-row--phone">
        <svg class="contact-icon" viewBox="0 0 42 42" aria-hidden="true">
          <rect x="2" y="2" width="38" height="38" rx="8" fill="none" stroke="#fff" stroke-width="3"/>
          <path d="M14 11 c2-1 3 0 4 2 l1.5 3.5 c0.5 1.2 0 2-1 2.8 l-1 0.8 c1 2.6 3 4.8 5.6 6 l0.9-1 c0.8-1 1.7-1.3 2.8-0.8 l3.4 1.6 c1.8 0.9 2.3 2 1.4 3.8 c-1 2-3 3-5.5 2.3 C19.5 30 12.5 23 11 16 c-0.6-2.5 0.8-4.2 3-5 z" fill="none" stroke="#fff" stroke-width="2"/>
        </svg>
        <p class="contact-text contact-text--phone">502-555-0147</p>
      </div>
    </div>
  </section>

  <section class="card card--back" aria-label="Business card, light blue version">
    <div class="identity">
      <h2 class="identity__name">Rev. Curtis Holloway</h2>
      <p class="identity__slogan">Honor God and Make Discies</p>
    </div>
    <div class="contact-panel">
      <div class="contact-row contact-row--address">
        <svg class="contact-icon" viewBox="0 0 42 42" aria-hidden="true">
          <rect x="2" y="2" width="38" height="38" rx="8" fill="none" stroke="#fff" stroke-width="3"/>
          <path d="M21 9 L32 19 H29 V31 H13 V19 H10 Z" fill="#fff"/>
          <rect x="16" y="21" width="4" height="4" fill="#0555a3"/>
          <rect x="22" y="21" width="4" height="4" fill="#0555a3"/>
        </svg>
        <p class="contact-text contact-text--address">2846 Willow Creek Rd.<br>Frankfort KY</p>
      </div>
      <div class="contact-row contact-row--phone">
        <svg class="contact-icon" viewBox="0 0 42 42" aria-hidden="true">
          <rect x="2" y="2" width="38" height="38" rx="8" fill="none" stroke="#fff" stroke-width="3"/>
          <path d="M14 11 c2-1 3 0 4 2 l1.5 3.5 c0.5 1.2 0 2-1 2.8 l-1 0.8 c1 2.6 3 4.8 5.6 6 l0.9-1 c0.8-1 1.7-1.3 2.8-0.8 l3.4 1.6 c1.8 0.9 2.3 2 1.4 3.8 c-1 2-3 3-5.5 2.3 C19.5 30 12.5 23 11 16 c-0.6-2.5 0.8-4.2 3-5 z" fill="none" stroke="#fff" stroke-width="2"/>
        </svg>
        <p class="contact-text contact-text--phone">502-555-0147</p>
      </div>
    </div>
  </section>

</main>
</body>
</html>
```